Relocation/furniture installation company needs new business cards

we are a relocation and furniture installation company mainly dealing with corporate clients and we are looking for new business card ideas. Cards should incorporate our logo and list our website, phone number and services. The company is only 2 years old but with more staff joining we are in the need for more business cards, so something with an awesome design that is eye catching would go a long way to insure we get our name out there and look good to potential new clients.

Target Market(s)

Corporate

Industry/Entity Type

Trade

Contact Information for Business Card

www.merovanta.co.nz
0508 7 kelpor

furniture installation
business relocations
joinery installation
commercial property maintenance

Colors
0592cd
34a7d8
85cae6
85acd3
0356a4
cfdfed
cee9f5
757575
474747

Requirements
Must have
• Business relocations and furniture installation specialists
Nice to have
• something that incorporates our logo.

```html
<!DOCTYPE html>
<html lang="en">
<head>
<meta charset="utf-8">
<title>Merovanta Business Cards</title>
<link href="https://fonts.googleapis.com/css2?family=Raleway:wght@300;400;500;600&display=swap" rel="stylesheet">
<style>
  :root {
    --bg: #2b2b2b;
    --card-grey: #757575;
    --card-white: #ffffff;
    --brand-blue: #0356a4;
    --brand-light: #34a7d8;
    --text-light: #ffffff;
    --text-soft: #e8e8e8;
  }
  * { margin: 0; padding: 0; box-sizing: border-box; }
  html, body {
    width: 1200px; height: 852px; overflow: hidden;
    background: var(--bg);
    font-family: "Raleway", sans-serif;
  }
  .stage {
    position: relative; width: 1200px; height: 852px;
    display: flex; align-items: center; justify-content: center; gap: 40px;
  }
  .card {
    position: relative; width: 540px; height: 310px;
    border-radius: 22px; overflow: hidden;
    box-shadow: 0 14px 30px rgba(0,0,0,.45);
  }
  .card--back {
    background: var(--card-grey);
    display: flex; align-items: center; justify-content: center;
  }
  .brand-name {
    font-weight: 600; letter-spacing: 4px; text-transform: uppercase;
    display: flex; align-items: center; gap: 12px;
  }
  .brand-name--back { color: var(--text-light); font-size: 40px; }
  .brand-mark {
    width: 34px; height: 34px; background: var(--brand-light);
  }
  .card--front { background: var(--card-white); }
  .front-logo {
    position: absolute; left: 0; top: 0; width: 236px; height: 310px;
    display: flex; align-items: center; justify-content: center;
  }
  .brand-name--front { color: var(--brand-blue); font-size: 24px; letter-spacing: 2px; gap: 8px; }
  .brand-name--front .brand-mark { width: 20px; height: 20px; background: var(--brand-blue); }
  .info-panel {
    position: absolute; left: 228px; top: 0; width: 312px; height: 310px;
    background: var(--card-grey);
    clip-path: polygon(8px 0, 100% 0, 100% 100%, 8px 100%, 8px 92px, 0 84px, 8px 76px);
    color: var(--text-light);
    padding: 48px 24px 0 36px;
  }
  .person-name { font-size: 24px; font-weight: 500; letter-spacing: 1px; text-transform: uppercase; line-height: 1; }
  .person-role { font-size: 12px; color: var(--text-soft); margin-top: 4px; }
  .contact-list { list-style: none; margin-top: 16px; font-size: 12.5px; font-weight: 300; }
  .contact-list li { display: flex; align-items: center; gap: 8px; line-height: 20px; }
  .contact-list svg { width: 10px; height: 10px; flex: none; fill: var(--text-light); }
  .contact-list .no-icon { padding-left: 18px; }
  .service-list { list-style: none; margin-top: 18px; font-size: 13px; font-weight: 300; line-height: 19px; }
</style>
</head>
<body>
<main class="stage">
  <section class="card card--back" aria-label="Card back">
    <div class="brand-name brand-name--back"><span class="brand-mark"></span>Merovanta</div>
  </section>

  <section class="card card--front" aria-label="Card front">
    <div class="front-logo">
      <div class="brand-name brand-name--front"><span class="brand-mark"></span>Merovanta</div>
    </div>
    <div class="info-panel">
      <h1 class="person-name">Arlen Tovey</h1>
      <p class="person-role">Director</p>
      <ul class="contact-list">
        <li><svg viewBox="0 0 10 10"><path d="M2 0.5l1.8 2.2-1 1.1a6 6 0 0 0 3.4 3.4l1.1-1L9.5 8 8 9.5C4 9.5 0.5 6 0.5 2z"/></svg>+330 4815 2093</li>
        <li><svg viewBox="0 0 10 10"><path d="M0.5 2h9v6h-9z M1.2 2.6 5 5.6 8.8 2.6" fill="none" stroke="#fff" stroke-width="1"/></svg>info@merovanta.co.nz</li>
        <li><svg viewBox="0 0 10 10"><circle cx="5" cy="5" r="4.3" fill="none" stroke="#fff" stroke-width="1"/><path d="M0.7 5h8.6M5 0.7c-2.4 2.6-2.4 6 0 8.6M5 0.7c2.4 2.6 2.4 6 0 8.6" fill="none" stroke="#fff" stroke-width=".8"/></svg>www.merovanta.co.nz</li>
        <li class="no-icon">0508 7 kelpor</li>
      </ul>
      <ul class="service-list">
        <li>furniture installation</li>
        <li>business relocations</li>
        <li>joinery installation</li>
        <li>commercial property maintenance</li>
      </ul>
    </div>
  </section>
</main>
</body>
</html>
```